Vessenby Office Partners needs a new interactive and interesting website

We need an interesting, professional, modern and functional company website for Vessenby Office Partners - a young IT Services company based out of Chennai, India.

Vessenby Office Partners is a fully owned subsidiary of Hollin Cellarworks, one of the world's leading direct to consumer wine merchant.

We already have a registered company logo which must feature in the website.

We conceive, design, develop, test, implement and support IT solutions across the entire Hollin Cellarworks IT landscape. For ex : We currently run about 25 e-commerce websites for Hollin Cellarworks on KVM and Dot Net.

We would like to see our corporate colors used in the website. (Burgundy wine and wine green - source: www.tallowmereop.example)

We are looking at this website to communicate a fun, friendly and professionally managed company - reaching out to career seekers, prospective customers and general public.

For reference - The company name 'Vessenby' is an inspiration from the Hollin Cellarworks lineage.

The second image with the world map is stickered on our main entrance to the office, I am not sure where this can be used -just putting it out there..
Updates

Please note that there are only a few more days to submit designs for this contest  !

I would appreciate if you can help posting your designs in time for our review and consideration.

Thanks.

Reason: Thanks for your inputs. We have a number of designers and a lot to digest and work with in the past few days. There has been a rush of new designs in the last few days Hence we will require more time to process these and make our decision. Hence i am requesting the contest to be open for more days. Regards, Suresh

Target Market(s)

Prospective job seekers who want to know more about the company and also wish to apply for a job vacancy
People wanting to know more about the company in general and our progress
People who want to see what we offer and how we can help them too - prospective customers
Companies that are interested in our IT Captive journey and are looking for a business opportunity

Industry/Entity Type

E-Commerce

Requirements
Must have
• Log In/ Register facility acting as a Single Sign on for Intranet (Employees)

Facility to post job vacancies (with an expiry date) and enable people to apply for a role and upload their CV/Resume.

Facility to Review Job applications

Facility for website visitors to contact Tallowmere Office Partners via an online 'Contact Us' form with a split of job seekers and business opportunities

Gallery facility to upload pictures regarding company events
Nice to have
• Less Cluttered and contemporary design
Some Wine/Vineyard inspirations will be good but not too much, the company is an IT services company

```html
<!DOCTYPE html>
<html lang="en">
<head>
<meta charset="utf-8">
<title>Vessenby Office Partners</title>
<link rel="stylesheet" href="https://fonts.googleapis.com/css2?family=Source+Sans+3:wght@400;600&family=Arimo:wght@400;700&display=swap">
<style>
  :root {
    --burgundy: #8c0f45;
    --burgundy-dark: #6e0a35;
    --paper: #efeae1;
    --paper-light: #f6f3ed;
    --band: #eeeeee;
    --nav-tab: #e4e0d8;
    --nav-text: #3d3a36;
    --body-text: #5a5650;
    --muted-text: #8a8782;
    --olive: #8a9a3a;
    --olive-light: #a9b84f;
    --footer: #3a3a3a;
    --white: #ffffff;
  }
  * { margin: 0; padding: 0; box-sizing: border-box; }
  html, body { width: 1200px; height: 923px; overflow: hidden; }
  body {
    position: relative;
    font-family: "Source Sans 3", "Helvetica Neue", Arial, sans-serif;
    background: var(--band);
  }
  .hero-backdrop {
    position: absolute; left: 0; top: 0; width: 1200px; height: 623px;
    background: linear-gradient(180deg, var(--paper-light) 0%, var(--paper) 45%, #e4ddd0 75%, #ddd5c6 100%);
  }
  .content-band {
    position: absolute; left: 0; top: 623px; width: 1200px; height: 224px;
    border-top: 4px solid var(--white);
    background: repeating-linear-gradient(135deg, #f1f1f1 0 3px, #ebebeb 3px 6px);
  }

  .brand { position: absolute; left: 120px; top: 0; width: 254px; height: 114px; }
  .brand svg { position: absolute; inset: 0; }
  .brand-name {
    position: absolute; left: 22px; top: 28px; width: 216px;
    color: var(--white); font-weight: 600; font-size: 23px; line-height: 27px;
  }

  .utility-links {
    position: absolute; right: 119px; top: 36px;
    display: flex; font-size: 15.5px;
  }
  .utility-links a { color: var(--burgundy-dark); text-decoration: none; padding: 0 12px; }
  .utility-links a + a { border-left: 1px dotted #c9c2b8; }
  .utility-links a:last-child { padding-right: 0; }

  .site-search {
    position: absolute; left: 840px; top: 81px; width: 241px; height: 33px;
    background: var(--white); border: 1px solid #cfcac2;
    font-size: 14px; color: #6b6863; padding: 7px 12px;
  }
  .site-search svg { position: absolute; right: 9px; top: 9px; }

  .main-nav { position: absolute; top: 163px; left: 0; width: 1200px; height: 53px; }
  .main-nav a {
    position: absolute; top: 0; height: 53px;
    display: flex; align-items: center; justify-content: center;
    background: var(--nav-tab); border-bottom: 5px solid var(--burgundy);
    color: var(--nav-text); text-decoration: none;
    font-family: "Arimo", Arial, sans-serif; font-size: 16.5px; letter-spacing: .3px;
  }
  .main-nav a.is-current { background: var(--white); }

  .feature-bottle {
    position: absolute; left: 122px; top: 289px; width: 88px; height: 311px;
    border-radius: 22px 22px 10px 10px;
    background: linear-gradient(90deg, #1c1016 0%, #3a2430 40%, #160b11 100%);
  }
  .feature-copy { position: absolute; left: 292px; top: 320px; width: 320px; }
  .feature-title { color: var(--burgundy); font-weight: 400; font-size: 30px; line-height: 40px; }
  .feature-text { margin-top: 10px; color: var(--body-text); font-size: 14.5px; line-height: 26.5px; }
  .feature-text span { display: block; white-space: nowrap; }
  .button-more {
    position: absolute; left: 292px; top: 473px; width: 126px; height: 42px;
    background: linear-gradient(180deg, #9c1752, var(--burgundy-dark));
    border: 1px solid #5c0a2d; border-radius: 3px; text-decoration: none;
    color: var(--white); font-size: 17px; display: flex; align-items: center; justify-content: center;
  }

  .event-slide {
    position: absolute; left: 659px; top: 287px; width: 422px; height: 336px;
    background: linear-gradient(135deg, #e9e6e1 0%, #cfcac3 45%, #8e8c89 70%, #dcdad6 100%);
  }
  .slide-arrow { position: absolute; top: 148px; }
  .slide-arrow.prev { left: 12px; }
  .slide-arrow.next { right: 16px; }

  .events-panel {
    position: absolute; left: 659px; top: 623px; width: 422px; height: 198px;
    background: linear-gradient(180deg, var(--olive) 0%, var(--olive-light) 100%);
    color: var(--white); padding: 16px 24px 0 21px;
  }
  .events-panel::before {
    content: ""; position: absolute; left: 53px; top: -10px;
    border-left: 10px solid transparent; border-right: 10px solid transparent;
    border-bottom: 10px solid var(--olive);
  }
  .events-title {
    font-weight: 400; font-size: 22.5px; line-height: 30px; padding-bottom: 10px;
    border-bottom: 1px solid rgba(255,255,255,.3);
  }
  .events-text { margin-top: 13px; font-size: 14.5px; line-height: 23.3px; font-weight: 600; }
  .events-text span { display: block; white-space: nowrap; }

  .welcome { position: absolute; left: 120px; top: 657px; width: 470px; }
  .welcome-title { font-weight: 400; font-size: 22.5px; line-height: 32px; color: #444; }
  .welcome-title span { color: var(--burgundy); }
  .welcome-text { margin-top: 10px; font-size: 13.8px; line-height: 23.3px; color: var(--muted-text); }
  .welcome-text span { display: block; white-space: nowrap; }

  .site-footer {
    position: absolute; left: 0; top: 847px; width: 1200px; height: 76px;
    background: var(--footer);
  }
  .copyright {
    position: absolute; left: 119px; top: 31px;
    font-family: "Arimo", Arial, sans-serif; font-size: 13px; color: #f0f0f0;
  }
  .social-links { position: absolute; left: 894px; top: 24px; display: flex; gap: 11px; }
  .social-links span { width: 34px; height: 34px; display: block; }
</style>
</head>
<body>
  <div class="hero-backdrop"></div>
  <div class="content-band"></div>

  <header>
    <div class="brand">
      <svg width="254" height="114" viewBox="0 0 254 114" aria-hidden="true">
        <path d="M0 0H254V114C200 100 150 96 110 104C70 112 30 112 0 106Z" fill="var(--burgundy)"/>
      </svg>
      <div class="brand-name">Vessenby Office Partners</div>
    </div>

    <nav class="utility-links">
      <a href="#">Careers</a>
      <a href="#">Contact</a>
    </nav>

    <div class="site-search">Search..
      <svg width="14" height="14" viewBox="0 0 14 14" aria-hidden="true">
        <circle cx="5.5" cy="5.5" r="4.3" fill="none" stroke="#9a9690" stroke-width="1.8"/>
        <path d="M8.7 8.7L12.8 12.8" stroke="#9a9690" stroke-width="2"/>
      </svg>
    </div>

    <nav class="main-nav">
      <a href="#" class="is-current" style="left:120px;width:112px">HOME</a>
      <a href="#" style="left:273px;width:127px">ABOUT US</a>
      <a href="#" style="left:446px;width:126px">CLIENTS</a>
      <a href="#" style="left:607px;width:126px">SERVICES</a>
      <a href="#" style="left:772px;width:127px">CAREERS</a>
      <a href="#" style="left:939px;width:142px">CONTACT US</a>
    </nav>
  </header>

  <main>
    <div class="feature-bottle" role="img" aria-label="Photo of a dark wine bottle with a white label"></div>
    <section class="feature-copy">
      <h2 class="feature-title">Aenean nec urna elitin</h2>
      <p class="feature-text">
        <span>Duis autem vel eum iriure dolor in hendrerit in</span>
        <span>vulputate velit esse molestie consequat, vel ill</span>
        <span>um dolore eu feugiat nulla facilisisat vero.</span>
      </p>
    </section>
    <a class="button-more" href="#">READ MORE</a>

    <div class="event-slide" role="img" aria-label="Photo of colleagues in a meeting room reviewing a company status dashboard on a monitor">
      <svg class="slide-arrow prev" width="30" height="30" viewBox="0 0 30 30" aria-hidden="true">
        <circle cx="15" cy="15" r="13" fill="rgba(0,0,0,.15)" stroke="#fff" stroke-width="2"/>
        <path d="M21 15H10M14 10L9 15L14 20" fill="none" stroke="#fff" stroke-width="2.4"/>
      </svg>
      <svg class="slide-arrow next" width="30" height="30" viewBox="0 0 30 30" aria-hidden="true">
        <circle cx="15" cy="15" r="13" fill="rgba(0,0,0,.15)" stroke="#fff" stroke-width="2"/>
        <path d="M9 15H20M16 10L21 15L16 20" fill="none" stroke="#fff" stroke-width="2.4"/>
      </svg>
    </div>

    <section class="events-panel">
      <h3 class="events-title">Company Events</h3>
      <p class="events-text">
        <span>Typi non habent claritatem insitam; est usus legentis nis qui</span>
        <span>facit eorum claritatem. Investigationes demonstraveruilecto</span>
        <span>res legere me lius quod ii legunt saepius. Claritas est etiapro</span>
        <span>cessus dynamicus, qui sequitur mutationem .</span>
      </p>
    </section>

    <section class="welcome">
      <h2 class="welcome-title">Welcome to <span>Vessenby</span></h2>
      <p class="welcome-text">
        <span>Typi non habent claritatem insitam; est usus legentis nis qui facit eorum clarita</span>
        <span>tem. Investigationes demonstraveruilectores legere me lius quod ii legunt saei</span>
        <span>pius. Claritas est etiaprocessus dynamicus, qui sequitur mutationem . Nullam v</span>
        <span>arius eleifend elit, nec sollicitudin est vulputate a. Suspendisse non elit ante.</span>
      </p>
    </section>
  </main>

  <footer class="site-footer">
    <p class="copyright">Copyright ©2013. All Rights Reserved.</p>
    <div class="social-links">
      <span style="background:#3a5a9c" aria-label="Social link"></span>
      <span style="background:#2f9ad6" aria-label="Social link"></span>
      <span style="background:#f26a1d" aria-label="Social link"></span>
      <span style="background:#e0262b" aria-label="Social link"></span>
    </div>
  </footer>
</body>
</html>
```